Brandvale Site Oversight Group Inc. needs a logo design (BSOGI) and a business card design

We need a logo design and business card design for a new company. Simple yet elegant/stylish and professional. to the point. Focal point BRANDVALE...underneith Site Oversight Group Inc smaller font. Plus a logo that can be on the opposite side of the business card and used for T-Shirts.
Back back ground, silver/grey font. I like the look of Quirtle Studio logo
Target Market(s)
Project controls, Planning, Scheduling, Engineering, Project Management
Industry/Entity Type
Business
Contact Information for Business Card
Company name on one side, logo and details on the other
Font styles to use
Requirements
Must have
- Delphine Brandvale
- Project Planner
- BrandvaleSOGI@postmarrow.example
- P.O. Box 9
- Fernhollow WM NORLAND
- X9Q2R7
- +1 (555) 284 3917
Nice to have
- Your input :) quote "Fail to plan, plan to fail"
Should not have
- Too much!

```html
<!DOCTYPE html>
<html lang="en">
<head>
<meta charset="utf-8">
<title>Brandvale Site Oversight Group Inc. — Business Card</title>
<link rel="stylesheet" href="https://fonts.googleapis.com/css2?family=PT+Serif:wght@400;700&display=swap">
<style>
  :root {
    --backdrop: #2b2826;
    --card: #0d0d0d;
    --card-edge: #1c1c1c;
    --ink: #f2f2f2;
    --silver: #b9b9b9;
    --rule: #9a9a9a;
  }
  * { margin: 0; padding: 0; box-sizing: border-box; }
  html, body { width: 1200px; height: 716px; overflow: hidden; }
  body {
    background: var(--backdrop);
    font-family: "PT Serif", Georgia, serif;
    position: relative;
  }
  .card {
    position: absolute;
    width: 540px;
    height: 310px;
    background: var(--card);
    border: 1px solid var(--card-edge);
    box-shadow: 0 14px 30px rgba(0,0,0,0.45);
    overflow: hidden;
  }
  .card--front { left: 40px; top: 203px; }
  .card--back { left: 620px; top: 203px; }

  .wordmark {
    position: absolute;
    width: 300px;
    text-align: center;
    color: var(--ink);
  }
  .wordmark__name {
    font-weight: 700;
    font-size: 40px;
    letter-spacing: 1px;
    line-height: 1;
  }
  .wordmark__rule {
    display: flex;
    align-items: center;
    gap: 8px;
    margin-top: 10px;
    height: 12px;
  }
  .wordmark__line {
    flex: 1;
    border-top: 1px solid var(--rule);
  }
  .wordmark__tagline {
    font-size: 8px;
    letter-spacing: 1px;
    line-height: 12px;
    color: var(--silver);
    white-space: nowrap;
  }
  .card--front .wordmark { left: 120px; top: 122px; }
  .card--back .wordmark {
    left: -100px;
    top: 120px;
    width: 280px;
    transform: rotate(-90deg);
  }
  .card--back .wordmark__name { font-size: 36px; }

  .contact {
    position: absolute;
    left: 300px;
    top: 172px;
    color: var(--ink);
  }
  .contact__name { font-size: 16px; letter-spacing: 0.5px; }
  .contact__title { font-size: 11px; color: var(--silver); }
  .contact__rule {
    width: 190px;
    border-top: 1px solid var(--rule);
    margin: 6px 0 8px;
  }
  .contact__line { font-size: 11px; line-height: 15px; color: var(--ink); }
</style>
</head>
<body>
  <section class="card card--front" aria-label="Card front">
    <div class="wordmark">
      <div class="wordmark__name">BRANDVALE</div>
      <div class="wordmark__rule">
        <span class="wordmark__line"></span>
        <span class="wordmark__tagline">SITE OVERSIGHT GROUP</span>
        <span class="wordmark__line"></span>
      </div>
    </div>
  </section>

  <section class="card card--back" aria-label="Card back">
    <div class="wordmark">
      <div class="wordmark__name">BRANDVALE</div>
      <div class="wordmark__rule">
        <span class="wordmark__line"></span>
        <span class="wordmark__tagline">SITE OVERSIGHT GROUP</span>
        <span class="wordmark__line"></span>
      </div>
    </div>
    <div class="contact">
      <div class="contact__name">Delphine Brandvale</div>
      <div class="contact__title">Project Planner</div>
      <div class="contact__rule"></div>
      <div class="contact__line">+1 (555) 284 3917</div>
      <div class="contact__line">BrandvaleSOGI@postmarrow.example</div>
      <div class="contact__line">P.O. Box 9, Fernhollow WM NORLAND, X9Q2R7</div>
    </div>
  </section>
</body>
</html>
```